Harborline Motors LLC

Car Dealer Customer Service
Address: 2741 Linden Avenue, Shelbyville, TN 37162
web: www.harborlinemotorstn.net
email: harborlinemotorstn@mailbox-example.net
Phone: (931) 555-0148
Phone: (629) 555-0173

```html
<!DOCTYPE html>
<html lang="en">
<head>
<meta charset="utf-8">
<title>Harborline Motors LLC — Business Card</title>
<link href="https://fonts.googleapis.com/css2?family=Barlow+Condensed:wght@400;700&display=swap" rel="stylesheet">
<style>
  :root {
    --page: #cacaca;
    --brand-blue: #2688c9;
    --sky-blue: #3db6f7;
    --accent-yellow: #ebab33;
    --paper: #ffffff;
  }
  html, body {
    margin: 0;
    padding: 0;
    width: 1200px;
    height: 846px;
    overflow: hidden;
    background: var(--page);
    font-family: "Barlow Condensed", "Arial Narrow", sans-serif;
  }
  .card {
    position: absolute;
    left: 346px;
    width: 509px;
    height: 290px;
    overflow: hidden;
  }
  .card--front { top: 114px; display: flex; }
  .card--back {
    top: 444px;
    background: radial-gradient(circle at 50% 52%, var(--sky-blue) 0%, #30a0e0 30%, var(--brand-blue) 62%);
  }

  .front__brand {
    width: 256px;
    background: var(--paper);
    border: 1px solid #111;
    border-right: none;
    box-sizing: border-box;
    position: relative;
  }
  .brand__dot {
    position: absolute;
    left: 50%;
    top: 96px;
    width: 88px;
    height: 88px;
    margin-left: -44px;
    margin-top: -44px;
    border-radius: 50%;
    background: var(--sky-blue);
  }
  .brand__name {
    position: absolute;
    left: 0;
    right: 0;
    top: 190px;
    text-align: center;
    font-weight: 700;
    font-size: 26px;
    letter-spacing: 0.5px;
    color: var(--brand-blue);
    line-height: 1;
  }

  .front__stripe { width: 8px; background: var(--accent-yellow); }

  .front__contact {
    flex: 1;
    background: var(--brand-blue);
    border: 1px solid #111;
    border-left: none;
    box-sizing: border-box;
    position: relative;
    color: var(--accent-yellow);
  }
  .contact-row {
    position: absolute;
    left: 26px;
    right: 6px;
    display: flex;
    align-items: center;
    gap: 7px;
    font-size: 16px;
    line-height: 1;
    white-space: nowrap;
  }
  .contact-row svg { width: 17px; height: 17px; flex: none; }
  .contact-row--email { font-size: 11.5px; }
  .contact-row--address { align-items: flex-start; font-size: 16px; line-height: 20px; }
  .contact-row--address svg { height: 26px; margin-top: 2px; }

  .back__name {
    position: absolute;
    left: 0;
    right: 0;
    top: 122px;
    text-align: center;
    font-weight: 700;
    font-size: 44px;
    letter-spacing: 1px;
    color: var(--accent-yellow);
    line-height: 1;
  }
</style>
</head>
<body>

<section class="card card--front" aria-label="Business card front">
  <div class="front__brand">
    <span class="brand__dot"></span>
    <div class="brand__name">HARBORLINE MOTORS</div>
  </div>
  <div class="front__stripe"></div>
  <div class="front__contact">
    <div class="contact-row" style="top:86px">
      <svg viewBox="0 0 24 24" fill="none" stroke="currentColor" stroke-width="2" stroke-linecap="round" stroke-linejoin="round"><path d="M5 3h3l2 5-2 1.5a11 11 0 0 0 6.5 6.5L16 14l5 2v3a2 2 0 0 1-2 2A17 17 0 0 1 3 5a2 2 0 0 1 2-2z"/><path d="M14 3a7 7 0 0 1 7 7M14 7a3 3 0 0 1 3 3"/></svg>
      <span>(931) 555-0148</span>
    </div>
    <div class="contact-row" style="top:108px">
      <svg viewBox="0 0 24 24" fill="none" stroke="currentColor" stroke-width="2" stroke-linecap="round" stroke-linejoin="round"><path d="M5 3h3l2 5-2 1.5a11 11 0 0 0 6.5 6.5L16 14l5 2v3a2 2 0 0 1-2 2A17 17 0 0 1 3 5a2 2 0 0 1 2-2z"/><path d="M14 3a7 7 0 0 1 7 7M14 7a3 3 0 0 1 3 3"/></svg>
      <span>(629) 555-0173</span>
    </div>
    <div class="contact-row contact-row--email" style="top:131px">
      <svg viewBox="0 0 24 24" fill="currentColor"><path d="M2 5h20v14H2z"/><path d="M2 5l10 8 10-8M2 19l7-7M22 19l-7-7" fill="none" stroke="#2688c9" stroke-width="1.5"/></svg>
      <span>harborlinemotorstn@mailbox-example.net</span>
    </div>
    <div class="contact-row" style="top:153px">
      <svg viewBox="0 0 24 24" fill="none" stroke="currentColor" stroke-width="2"><circle cx="12" cy="12" r="10"/><ellipse cx="12" cy="12" rx="4" ry="10"/><path d="M2 12h20M4 7h16M4 17h16"/></svg>
      <span>www.harborlinemotorstn.net</span>
    </div>
    <div class="contact-row contact-row--address" style="top:193px">
      <svg viewBox="0 0 20 28" fill="currentColor"><path d="M10 0a10 10 0 0 0-10 10c0 7 10 18 10 18s10-11 10-18A10 10 0 0 0 10 0zm0 14a4 4 0 1 1 0-8 4 4 0 0 1 0 8z"/></svg>
      <span>2741 Linden Avenue,<br>Shelbyville, TN 37162</span>
    </div>
  </div>
</section>

<section class="card card--back" aria-label="Business card back">
  <div class="back__name">HARBORLINE MOTORS</div>
</section>

</body>
</html>
```